Brindle and Oak Products

We are wanting product labels for a larder range. Designs almost complete. Some of the details will need to be slightly changed on the XLS files.

```html
<!DOCTYPE html>
<html lang="en">
<head>
<meta charset="utf-8">
<title>Brindle and Oak – Relish Simmer Sauce Label</title>
<link href="https://fonts.googleapis.com/css2?family=Bebas+Neue&family=Great+Vibes&family=Roboto:wght@400&display=swap" rel="stylesheet">
<style>
  :root {
    --label-black: #111111;
    --label-black-edge: #1c1c1c;
    --rose-light: #f3d3d3;
    --rose: #d8a0a0;
    --rose-deep: #b8696b;
    --paper-white: #f4f4f4;
    --canvas-bg: #ffffff;
    --ink: #111111;
  }
  * { margin: 0; padding: 0; box-sizing: border-box; }
  html, body {
    width: 1187px;
    height: 1200px;
    overflow: hidden;
    background: var(--canvas-bg);
  }
  .canvas {
    position: relative;
    width: 1187px;
    height: 1200px;
  }
  .label {
    position: absolute;
    left: 296px;
    top: 374px;
    width: 556px;
    height: 578px;
    background: linear-gradient(90deg, var(--label-black-edge), var(--label-black) 20%, var(--label-black) 80%, var(--label-black-edge));
  }
  .brand-mark {
    position: absolute;
    left: 374px;
    top: 408px;
    width: 216px;
    height: 216px;
  }
  .brand-mark__ring {
    position: absolute;
    inset: 0;
    border: 1.5px solid var(--rose);
    border-radius: 50%;
  }
  .brand-mark__name {
    position: absolute;
    inset: 0;
    display: flex;
    align-items: center;
    justify-content: center;
    text-align: center;
    font-family: "Bebas Neue", sans-serif;
    font-size: 44px;
    line-height: 0.95;
    letter-spacing: 1px;
    color: var(--rose);
  }
  .product-name {
    position: absolute;
    left: 374px;
    top: 660px;
    font-family: "Bebas Neue", sans-serif;
    font-size: 98px;
    line-height: 1;
    color: var(--paper-white);
    letter-spacing: 1px;
  }
  .product-type {
    position: absolute;
    left: 374px;
    top: 762px;
    font-family: "Bebas Neue", sans-serif;
    font-size: 50px;
    line-height: 1;
    letter-spacing: 5px;
    background: linear-gradient(90deg, var(--rose-light), var(--rose) 45%, var(--rose-deep));
    -webkit-background-clip: text;
    background-clip: text;
    color: transparent;
  }
  .divider {
    position: absolute;
    left: 375px;
    top: 828px;
    width: 375px;
    border-top: 2px dotted var(--paper-white);
  }
  .tagline {
    position: absolute;
    left: 374px;
    top: 842px;
    font-family: "Great Vibes", cursive;
    font-size: 29px;
    color: var(--paper-white);
    white-space: nowrap;
  }
  .weight-band {
    position: absolute;
    left: 296px;
    top: 916px;
    width: 556px;
    height: 23px;
    background: linear-gradient(90deg, var(--rose-light), var(--rose) 50%, var(--rose-deep));
    font-family: "Roboto", sans-serif;
    font-size: 15px;
    line-height: 23px;
    color: var(--ink);
    padding-left: 208px;
  }
  .flavour-tab {
    position: absolute;
    left: 650px;
    top: 164px;
    width: 92px;
    height: 411px;
    background: linear-gradient(90deg, var(--rose-deep), var(--rose) 35%, var(--rose) 65%, var(--rose-deep));
  }
  .flavour-tab__stitch {
    position: absolute;
    left: 9px;
    right: 9px;
    top: 0;
    bottom: 9px;
    border: 1.5px dashed var(--ink);
    border-top: none;
  }
  .flavour-tab__text {
    position: absolute;
    left: 50%;
    bottom: 42px;
    transform-origin: left center;
    transform: translateX(-50%) rotate(-90deg) translateX(0);
    font-family: "Bebas Neue", sans-serif;
    font-size: 40px;
    letter-spacing: 1.5px;
    color: var(--ink);
    white-space: nowrap;
  }
  .flavour-tab__text {
    left: 64px;
    bottom: 30px;
    transform: rotate(-90deg);
    transform-origin: left bottom;
  }
</style>
</head>
<body>
<main class="canvas">
  <section class="label" aria-label="Relish simmer sauce product label"></section>

  <div class="brand-mark">
    <span class="brand-mark__ring"></span>
    <span class="brand-mark__name">Brindle<br>and Oak</span>
  </div>

  <h1 class="product-name">RELISH</h1>
  <p class="product-type">·SIMMER SAUCE·</p>
  <div class="divider"></div>
  <p class="tagline">An Indian curry full of heat and flavour</p>
  <div class="weight-band">375 gm</div>

  <div class="flavour-tab">
    <span class="flavour-tab__stitch"></span>
    <span class="flavour-tab__text">INDIAN CHUTNEY</span>
  </div>
</main>
</body>
</html>
```